vorp business card design

vorp is an incubator within TRW Mediaworks focused on unlocking the potential in underserved niche micro-verticals on the web. our mission is to rapidly develop and foster emerging micro-verticals bc they are ripe for growth - building interesting and trusted content experiences with unqiue, useful and cutting-edge delivery methods.please do all copy (except for TRW Mediaworks, which must look as typed here and in logo) in all lowercase. Also please use spaces between phone # extensions not dashes or periods. I have attached all variations of the logo.
Industry/Entity Type
Business
Contact Information for Business Card
dale fenwright, ceo www.vorp.example 218 9th avenue 3rd floor oakland ca 94610 415 602 0002m 510 985 7966d dale.fenwright@vorp.example
Look and feel

```html
<!DOCTYPE html>
<html lang="en">
<head>
<meta charset="utf-8">
<title>vorp business card</title>
<link rel="stylesheet" href="https://fonts.googleapis.com/css2?family=Source+Sans+3:wght@400;600&display=swap">
<style>
  :root {
    --page-bg: #e9e7e4;
    --card-bg: #fbfbfa;
    --card-edge: #dcdad6;
    --ink: #1f1d1e;
    --teal: #16807c;
  }
  * { margin: 0; padding: 0; box-sizing: border-box; }
  html, body {
    width: 1200px; height: 900px; overflow: hidden;
    background: var(--page-bg);
    font-family: "Source Sans 3", sans-serif;
    color: var(--ink);
  }
  .business-card {
    position: absolute;
    left: 100px; top: 144px;
    width: 1000px; height: 612px;
    background: var(--card-bg);
    border: 1px solid var(--card-edge);
    border-radius: 26px;
    box-shadow: 0 10px 30px rgba(0,0,0,0.08);
  }
  .identity { position: absolute; left: 49px; top: 56px; }
  .identity__name {
    font-size: 35px; font-weight: 600; color: var(--teal); line-height: 1;
  }
  .identity__title { font-size: 25px; line-height: 1.2; margin-top: 6px; }
  .identity__address {
    font-size: 25px; line-height: 1.45; margin-top: 26px; width: 300px;
  }
  .contact-list {
    position: absolute; right: 48px; top: 68px;
    list-style: none;
  }
  .contact-list__item {
    display: flex; justify-content: flex-end; align-items: center;
    font-size: 25px; line-height: 1; height: 42px; gap: 14px;
  }
  .contact-list__icon { width: 20px; height: 20px; fill: var(--teal); flex: none; }
  .contact-list__icon--stroke { fill: none; stroke: var(--teal); stroke-width: 2.4; }
  .brand {
    position: absolute; left: 238px; top: 318px;
    display: flex; align-items: center; gap: 20px;
  }
  .brand__name {
    font-size: 150px; font-weight: 600; color: var(--ink); line-height: 1;
    letter-spacing: 2px;
  }
  .brand__dot {
    width: 46px; height: 46px; border-radius: 50%; background: var(--teal);
    margin-top: 40px;
  }
  .brand__tagline {
    position: absolute; left: 244px; top: 496px;
    font-size: 29px; line-height: 1;
  }
</style>
</head>
<body>
  <div class="business-card">
    <div class="identity">
      <div class="identity__name">Dale Fenwright</div>
      <div class="identity__title">CEO</div>
      <div class="identity__address">218 9th avenue 3rd floor oakland ca 94610</div>
    </div>

    <ul class="contact-list">
      <li class="contact-list__item">415 738 1194
        <svg class="contact-list__icon" viewBox="0 0 24 24"><path d="M6.6 10.8a15.1 15.1 0 0 0 6.6 6.6l2.2-2.2c.3-.3.7-.4 1-.2 1.1.4 2.3.6 3.6.6.6 0 1 .4 1 1V20c0 .6-.4 1-1 1A17 17 0 0 1 3 4c0-.6.4-1 1-1h3.5c.6 0 1 .4 1 1 0 1.3.2 2.5.6 3.6.1.3 0 .7-.2 1z"/></svg>
      </li>
      <li class="contact-list__item">510 247 3318
        <svg class="contact-list__icon" viewBox="0 0 24 24"><path d="M6.6 10.8a15.1 15.1 0 0 0 6.6 6.6l2.2-2.2c.3-.3.7-.4 1-.2 1.1.4 2.3.6 3.6.6.6 0 1 .4 1 1V20c0 .6-.4 1-1 1A17 17 0 0 1 3 4c0-.6.4-1 1-1h3.5c.6 0 1 .4 1 1 0 1.3.2 2.5.6 3.6.1.3 0 .7-.2 1z"/></svg>
      </li>
      <li class="contact-list__item">dale.fenwright@vorp.example
        <svg class="contact-list__icon" viewBox="0 0 24 24"><path d="M2 5h20v14H2z"/><path d="M2 5l10 8 10-8" fill="none" stroke="#fbfbfa" stroke-width="2"/></svg>
      </li>
      <li class="contact-list__item">www.vorp.example
        <svg class="contact-list__icon contact-list__icon--stroke" viewBox="0 0 24 24"><path d="M10 14a4 4 0 0 0 5.7 0l3.5-3.5a4 4 0 0 0-5.7-5.7l-1.2 1.2"/><path d="M14 10a4 4 0 0 0-5.7 0l-3.5 3.5a4 4 0 0 0 5.7 5.7l1.2-1.2"/></svg>
      </li>
    </ul>

    <div class="brand">
      <span class="brand__name">vorp</span>
      <span class="brand__dot"></span>
    </div>
    <div class="brand__tagline">a TRW Mediaworks incubator</div>
  </div>
</body>
</html>
```